Larkspur Ridge Management - Business Cards

I need business cards. My current logo was designed by a designer at this site and I very much like and am happy with the results. I would like a business card that is trendy, unique, current yet professional. I deal with high net worth clients daily

Target Market(s)

Out of state investors looking to get into the rental market in Ohio

Industry/Entity Type

Property Management, Consulting

Contact Information for Business Card

Name, Title (Chief Financial Officer) office phone number (555) 817-3094 website address larkridgemgmt.example

Font styles to use
Sans Serif

Colors
0054AA
0677BA
7BADD7
CADEEF
E8F1F8
0094D4
00A9DD
6FCCEA
C7EBF8
E9F6FB
00AB8E
00BBA5
67D7C9
C6EFE9
E9F9F6

```html
<!DOCTYPE html>
<html lang="en">
<head>
<meta charset="utf-8">
<title>Larkspur Ridge Management – Business Cards</title>
<link href="https://fonts.googleapis.com/css2?family=Montserrat:wght@500;600;700&display=swap" rel="stylesheet">
<style>
  :root {
    --paper: #f4f3ee;
    --navy: #152a4f;
    --navy-soft: #1b3360;
    --red: #c8232c;
    --gold: #b49a6a;
    --white: #ffffff;
    --ink: #1a2b4c;
    --line: #dfe3ea;
  }
  * { margin: 0; padding: 0; box-sizing: border-box; }
  html, body {
    width: 1200px; height: 1200px; overflow: hidden;
    background: var(--paper);
    font-family: "Montserrat", sans-serif;
    color: var(--ink);
  }
  .sheet { position: relative; width: 1200px; height: 1200px; }

  .card { position: absolute; top: 184px; height: 820px; box-shadow: 0 6px 18px rgba(0,0,0,0.12); }

  /* Front */
  .card-front {
    left: 91px; width: 483px;
    background: var(--gold);
    padding: 5px;
  }
  .front-field {
    position: relative; width: 100%; height: 100%;
    background: linear-gradient(160deg, var(--navy-soft), var(--navy));
  }
  .front-frame {
    position: absolute; left: 32px; right: 32px; top: 33px; bottom: 33px;
    border: 2px solid var(--red);
  }
  .front-name {
    position: absolute; left: 50px; right: 50px; top: 330px;
    text-align: center; color: var(--white);
    font-weight: 700; font-size: 44px; line-height: 1.15;
    text-transform: uppercase; letter-spacing: 1px;
  }
  .front-mark {
    position: absolute; left: 50%; top: 290px; width: 22px; height: 22px;
    margin-left: -11px; background: var(--red);
  }

  /* Back */
  .card-back {
    left: 627px; width: 484px;
    background: var(--white);
    overflow: hidden;
  }
  .back-band {
    position: absolute; left: 0; top: 0; width: 100%; height: 232px;
    background: var(--navy);
    border-bottom: 8px solid var(--red);
  }
  .back-brand {
    position: absolute; right: 38px; top: 92px; width: 170px;
    text-align: center; color: var(--white);
    font-weight: 700; font-size: 18px; line-height: 1.2; text-transform: uppercase;
  }
  .back-details {
    position: absolute; right: 56px; top: 320px; text-align: right;
  }
  .person-name { font-weight: 700; font-size: 53px; color: var(--navy); letter-spacing: -0.5px; line-height: 1; }
  .person-title { margin-top: 22px; font-weight: 500; font-size: 29px; color: var(--ink); }
  .divider { width: 356px; height: 3px; background: var(--gold); margin: 24px 0 0 auto; }
  .contact { list-style: none; margin-top: 30px; }
  .contact-item {
    display: flex; justify-content: flex-end; align-items: center; gap: 14px;
    font-weight: 500; font-size: 28px; color: var(--ink); height: 34px; margin-bottom: 22px;
  }
  .contact-icon { width: 30px; height: 30px; border-radius: 5px; background: var(--navy); display: block; }
  .back-pattern {
    position: absolute; left: 0; bottom: 0; width: 100%; height: 220px;
    background: linear-gradient(180deg, var(--white), var(--line));
  }

  .label {
    position: absolute; top: 1042px;
    font-weight: 600; font-size: 30px; letter-spacing: 1px; color: var(--navy);
    text-align: center;
  }
  .label-front { left: 91px; width: 483px; }
  .label-back { left: 627px; width: 484px; }
</style>
</head>
<body>
<main class="sheet">
  <section class="card card-front">
    <div class="front-field" role="img" aria-label="Navy background with faint architectural blueprint lines">
      <div class="front-frame"></div>
      <span class="front-mark"></span>
      <p class="front-name">Larkspur Ridge Management</p>
    </div>
  </section>

  <section class="card card-back">
    <header class="back-band">
      <p class="back-brand">Larkspur Ridge Management</p>
    </header>
    <div class="back-details">
      <h1 class="person-name">Narro Name</h1>
      <p class="person-title">Chief Financial Officer</p>
      <div class="divider"></div>
      <ul class="contact">
        <li class="contact-item">
          <span>(555) 817-3094</span>
          <svg class="contact-icon" viewBox="0 0 30 30" aria-hidden="true">
            <rect width="30" height="30" rx="5" fill="#152a4f"/>
            <path d="M10 7.5l3 0.5 1.3 3.6-1.9 1.4a10 10 0 0 0 4.6 4.6l1.4-1.9 3.6 1.3 0.5 3a2 2 0 0 1-2 2A14.5 14.5 0 0 1 8 10a2 2 0 0 1 2-2.5z" fill="#ffffff"/>
          </svg>
        </li>
        <li class="contact-item">
          <span>larkridgemgmt.example</span>
          <svg class="contact-icon" viewBox="0 0 30 30" aria-hidden="true">
            <rect width="30" height="30" rx="5" fill="#152a4f"/>
            <g fill="none" stroke="#ffffff" stroke-width="1.6">
              <circle cx="15" cy="15" r="7.5"/>
              <ellipse cx="15" cy="15" rx="3.3" ry="7.5"/>
              <line x1="7.5" y1="15" x2="22.5" y2="15"/>
            </g>
          </svg>
        </li>
      </ul>
    </div>
    <div class="back-pattern" role="img" aria-label="Fine navy blueprint line drawing along the bottom of the card"></div>
  </section>

  <p class="label label-front">FRONT SIDE</p>
  <p class="label label-back">BACK SIDE</p>
</main>
</body>
</html>
```